label design for coffee bean packaging

Logo will be provided. Label design for package of coffee beans for a micro roasted coffee company. Need to have space to write in origin, weight with check box for 1/4, 1/2, 1lb. Need to have check boxes for Light, Medium, Dark. Creative unique label design with boarders and fun, modern design. Company name is Cedar Brook Roasting Company. See attached logo. I have source files for logo if needed for design.
Industry/Entity Type
Coffee Shop
Font styles to use
Other font styles liked:
- Montez, kautiva cyrillic, uniform bold
Colors
f78f20
faa54b
f37122
fece3e
acd036
Requirements
Must have
- logo included in the design

```html
<!DOCTYPE html>
<html lang="en">
<head>
<meta charset="utf-8">
<title>Cedar Brook Roasting Company – Coffee Bean Label</title>
<link href="https://fonts.googleapis.com/css2?family=Kanit:wght@600&display=swap" rel="stylesheet">
<style>
  :root {
    --brown: #7a4e32;
    --brown-dark: #5a3119;
    --orange: #f28e22;
    --orange-light: #faa54b;
    --yellow: #fece3e;
    --white: #ffffff;
    --paper: #ffffff;
  }
  html, body {
    margin: 0;
    padding: 0;
    width: 1200px;
    height: 1000px;
    overflow: hidden;
    background: var(--paper);
  }
  .label {
    display: block;
    width: 1200px;
    height: 1000px;
  }
  .frame-outer { fill: var(--white); stroke: var(--brown); stroke-width: 4; }
  .frame-yellow { fill: none; stroke: var(--yellow); stroke-width: 2.5; }
  .frame-orange { fill: none; stroke: var(--orange); stroke-width: 7; }
  .frame-inner-yellow { fill: none; stroke: var(--yellow); stroke-width: 2; }
  .brand-ring { fill: var(--white); stroke: var(--brown-dark); stroke-width: 3; }
  .brand-name {
    font-family: "Kanit", sans-serif;
    font-weight: 600;
    fill: var(--brown-dark);
    text-anchor: middle;
  }
  .divider-line { stroke: var(--brown); stroke-width: 3; }
  .divider-dot { fill: var(--brown); }
  .origin-band { fill: url(#bandTone); }
  .origin-field-back { fill: var(--white); }
  .origin-field { fill: var(--white); stroke: var(--brown-dark); stroke-width: 2; }
  .info-bar { fill: var(--orange); }
  .roast-badge-ring { fill: var(--orange); }
  .roast-badge-face { fill: var(--white); stroke: var(--white); }
  .roast-badge-line { fill: none; stroke: var(--brown); stroke-width: 2; }
  .roast-badge-art { fill: var(--brown); }
  .icon-white { fill: var(--white); }
  .icon-stroke { fill: none; stroke: var(--white); stroke-width: 5; }
  .icon-text {
    font-family: "Kanit", sans-serif;
    font-weight: 600;
    fill: var(--brown);
    text-anchor: middle;
  }
  .website {
    font-family: "Kanit", sans-serif;
    font-weight: 600;
    font-size: 20px;
    fill: var(--white);
    text-anchor: middle;
    letter-spacing: 0.3px;
  }
</style>
</head>
<body>
<svg class="label" viewBox="0 0 1200 1000" xmlns="http://www.w3.org/2000/svg">
  <defs>
    <linearGradient id="bandTone" x1="0" x2="1" y1="0" y2="0">
      <stop offset="0" stop-color="#f7a233"/>
      <stop offset="0.5" stop-color="#f9b23d"/>
      <stop offset="1" stop-color="#f7a233"/>
    </linearGradient>
  </defs>

  <!-- Label frame -->
  <path class="frame-outer" d="M328,813 V273 H430 C455,190 520,150 596,150 C672,150 737,190 762,273 H864 V813 Z"/>
  <path class="frame-yellow" d="M336,805 V281 H437 C462,200 525,160 596,160 C667,160 730,200 755,281 H856 V805 Z"/>
  <path class="frame-orange" d="M344,797 V290 H445 C470,212 530,172 596,172 C662,172 722,212 747,290 H848 V797 Z"/>
  <path class="frame-inner-yellow" d="M352,789 V298 H452 C476,222 534,182 596,182 C658,182 716,222 740,298 H840 V789 Z"/>

  <!-- Brand name block -->
  <g class="brand">
    <circle class="brand-ring" cx="595" cy="300" r="109"/>
    <text class="brand-name" x="595" y="296" font-size="34">Cedar Brook</text>
    <text class="brand-name" x="595" y="326" font-size="20">Roasting Company</text>
  </g>

  <!-- Upper divider -->
  <line class="divider-line" x1="473" y1="431" x2="718" y2="431"/>
  <circle class="divider-dot" cx="596" cy="431" r="7"/>

  <!-- Origin write-in band -->
  <rect class="origin-band" x="360" y="443" width="472" height="112"/>
  <rect class="origin-field-back" x="408" y="455" width="372" height="88" rx="8"/>
  <rect class="origin-field" x="416" y="461" width="357" height="77" rx="8"/>

  <!-- Lower divider -->
  <line class="divider-line" x1="474" y1="573" x2="720" y2="573"/>
  <circle class="divider-dot" cx="597" cy="573" r="7"/>

  <!-- Info bar -->
  <rect class="info-bar" x="362" y="668" width="464" height="107"/>

  <!-- Roast badge -->
  <circle class="roast-badge-ring" cx="595" cy="665" r="57"/>
  <circle class="roast-badge-face" cx="595" cy="665" r="49"/>
  <circle class="roast-badge-line" cx="595" cy="665" r="45"/>
  <circle class="roast-badge-art" cx="595" cy="665" r="30" role="img" aria-label="Coffee beans illustration"/>

  <!-- Roast level: cup icon -->
  <g class="roast-level">
    <path class="icon-white" d="M392,678 H463 V700 C463,718 448,727 428,727 C407,727 392,718 392,700 Z"/>
    <path class="icon-stroke" d="M462,688 C478,684 478,703 460,707"/>
    <rect class="icon-white" x="386" y="727" width="82" height="6" rx="3"/>
    <text class="icon-text" x="426" y="704" font-size="17">Light</text>
  </g>

  <!-- Weight: bag icon -->
  <g class="weight">
    <path class="icon-white" d="M752,676 H795 L792,690 C802,700 802,726 795,738 H752 C745,726 745,700 755,690 Z"/>
    <text class="icon-text" x="773" y="722" font-size="22">1/4</text>
  </g>

  <!-- Website -->
  <text class="website" x="596" y="762">www.cedarbrookroastingcompany.com</text>
</svg>
</body>
</html>
```